Small Accounting Practice needs something creative

We need a business card design for a new small accounting practice based in Perth, Australia. The name of the practice is 'Kowra Ledger Partners Pty Ltd'. We providing Tax, Bookkeeping and Accounting services. Our target are individuals and small businesses. We want the design to be simply and creative. Also, we can the design can help us to gain people's trust.

Target Market(s)

Individuals and small businesses.

Industry/Entity Type

Accounting

Colors

Designer to choose colors to be used in the design.

```html
<!DOCTYPE html>
<html lang="en">
<head>
<meta charset="utf-8">
<title>Kowra Ledger Partners – Business Card</title>
<link href="https://fonts.googleapis.com/css2?family=Federo&family=Arvo:wght@400;700&family=Oswald:wght@400&display=swap" rel="stylesheet">
<style>
  :root {
    --page: #ffffff;
    --card-front: #f3f3f4;
    --card-back: #000000;
    --ink: #6e5f5a;
    --ink-edge: #2e2422;
    --ink-back: #8b817d;
    --shadow: rgba(0,0,0,0.55);
  }
  * { margin: 0; padding: 0; box-sizing: border-box; }
  html, body {
    width: 1200px; height: 1000px; overflow: hidden;
    background: var(--page);
  }
  .canvas { position: relative; width: 1200px; height: 1000px; }
  .card {
    position: absolute;
    box-shadow: 14px 14px 14px var(--shadow);
    overflow: hidden;
  }
  .card--front {
    left: 223px; top: 75px; width: 737px; height: 382px;
    background: var(--card-front);
  }
  .card--back {
    left: 224px; top: 507px; width: 734px; height: 383px;
    background: var(--card-back);
  }
  .card__photo {
    position: absolute; inset: 0;
    background:
      radial-gradient(ellipse at 25% 20%, #d9d9dc 0%, rgba(230,230,232,0) 45%),
      linear-gradient(170deg, #e4e4e6 0%, #f2f2f3 45%, #ebebed 100%);
  }
  .front-text {
    position: absolute; left: 0; right: 0; text-align: center;
    color: var(--ink);
    text-shadow: 0 0 1px var(--ink-edge), 1px 1px 0 var(--ink-edge), 2px 2px 2px rgba(0,0,0,0.25);
  }
  .role-title {
    top: 78px; font-family: "Federo", serif; font-size: 25px; letter-spacing: 0.3px;
  }
  .person-name {
    top: 156px; font-family: "Arvo", serif; font-size: 42px; font-weight: 400; letter-spacing: 1px;
  }
  .agent-line {
    top: 204px; font-family: "Arvo", serif; font-size: 21px; font-weight: 700; letter-spacing: 0.5px;
  }
  .email-line {
    top: 286px; font-family: "Federo", serif; font-size: 20px;
  }
  .company-name {
    position: absolute; left: 0; right: 0; top: 152px; text-align: center;
    font-family: "Oswald", sans-serif; font-size: 52px; font-weight: 400;
    letter-spacing: -0.5px; color: var(--ink-back);
  }
</style>
</head>
<body>
<main class="canvas">
  <section class="card card--front">
    <div class="card__photo" role="img" aria-label="Faded photo of a calculator, pen and financial statements"></div>
    <p class="front-text role-title">Accountant &amp; Small Business Consultant</p>
    <h1 class="front-text person-name">Liam Arden</h1>
    <p class="front-text agent-line">Registered ASIC Agent 48170</p>
    <p class="front-text email-line">Email: liam@kowraledgerpartners.com.au</p>
  </section>
  <section class="card card--back">
    <h2 class="company-name">Kowra Ledger Partners Pty Ltd</h2>
  </section>
</main>
</body>
</html>
```